E-Commerce Custom Design Magento Standard Requirements For Marketing Agency

I need to revamp theme for a website www.plinthwavestudio.com and want to change name to www.plinthwavehomes.com I have logo attached. I need a custom e commerce website built that pops and grabs attention. My logo is silver and looks great on black background. Please just use all same content from existing website www.plinthwavestudio.com and use existing products that you see there.

Target Market(s)

REAL ESTATE AGENTS

Industry/Entity Type

Digital Marketing

Coding

Coded - Design and coding required

Number of Pages Required

5+ page

Colors

Designer to choose colors to be used in the design.

Requirements
Must have
• Please revamp entire website www.plinthwavestudio.com and use new logo attached. Domain name will be www.plinthwavehomes.com and will offer marketing services for real estate agents around the country and world. Specializing in digital marketing services such as Vellumly Ads, Pictoraze Ads, Quip Loop Ads, Zarbit Promoworks, Etc.
Nice to have
Should not have

```html
<!DOCTYPE html>
<html lang="en">
<head>
<meta charset="utf-8">
<title>Plinthwave Dashboard</title>
<link rel="stylesheet" href="https://fonts.googleapis.com/css2?family=Montserrat:wght@400;500&family=Roboto+Condensed:wght@300;400&family=Libre+Baskerville:wght@400;700&family=Crimson+Text&display=swap">
<style>
:root{
  --teal:#1fc6bf;
  --grey-tab:#5f5f5f;
  --card:#d6d6d6;
  --ink:#1a1a1a;
  --ring:#666;
  --footer:#141414;
  --chat:#3dbf7a;
  --line-light:#6bbf6a;
  --line-dark:#0f7a35;
  --dot-orange:#f05a14;
}
*{margin:0;padding:0;box-sizing:border-box}
html,body{width:1136px;height:1200px;overflow:hidden;background:#fff}
body{position:relative;font-family:"Montserrat",sans-serif;color:var(--ink)}
.abs{position:absolute}

.topbar{position:absolute;left:0;top:0;width:1136px;height:79px;background:var(--teal);color:#fff;font-family:"Roboto Condensed",sans-serif;font-weight:300}
.brand{left:132px;top:28px;font-family:"Montserrat",sans-serif;font-size:15px;letter-spacing:1px;color:#e8e8e8;display:flex;align-items:center;gap:6px}
.brand i{display:block;width:14px;height:14px;border-radius:50%;background:#e8e8e8}
.phone{left:312px;top:19px;font-size:30px}
.cart{left:562px;top:24px}
.badge{left:600px;top:22px;width:14px;height:14px;border-radius:50%;background:#e84a3a;font-size:9px;text-align:center;line-height:14px;font-family:"Montserrat",sans-serif}
.nav{top:29px;font-size:21px}
.avatar{left:906px;top:21px;width:29px;height:29px;border-radius:50%;background:#e6e6e6}
.user{left:940px;top:28px;font-family:"Crimson Text",serif;font-size:13px}

.side a{position:absolute;left:0;display:flex;align-items:center;justify-content:center;height:38px;width:101px;background:var(--grey-tab);color:#fff;font-size:15px;text-decoration:none}
.side a.active{width:125px;background:var(--teal)}

.stat{width:141px;height:92px;top:104px;background:var(--card);font-size:24px;line-height:28px;padding-top:0}
.stat svg{position:absolute;left:40px;top:20px}

.sec-title{font-family:"Libre Baskerville",serif;font-weight:700;font-size:34px;width:1136px;text-align:center}
.underline{height:3px;background:var(--teal)}

.donut{top:320px;width:170px;text-align:center}
.donut svg{display:block;margin:0 auto}
.donut .pct{position:absolute;left:0;top:76px;width:170px;font-size:16px}
.month{font-family:"Crimson Text",serif;font-size:19px;margin-top:4px}
.big{font-family:"Libre Baskerville",serif;font-weight:700;font-size:17px;margin-top:14px}
.blurb{font-size:8.6px;line-height:11px;width:152px;text-align:left;margin:4px auto 0}

.chart-title{left:445px;top:712px;font-size:13px}
.legend{font-size:7.5px;color:#999}
.side-text h3{font-family:"Crimson Text",serif;font-weight:400;font-size:20px;text-align:center}
.side-text p{font-size:8.6px;line-height:10.8px;width:370px}

.chat{left:910px;top:1058px;width:144px;height:51px;border-radius:8px;background:var(--chat);color:#fff;font-family:"Roboto Condensed",sans-serif;font-weight:300;font-size:21px;display:flex;align-items:center;gap:10px;padding-left:10px}

.footer{left:0;top:1093px;width:1136px;height:107px;background:var(--footer);color:#fff}
.flinks{left:204px;top:24px;font-family:"Roboto Condensed",sans-serif;font-weight:300;font-size:21px}
.ficons{left:757px;top:16px;display:flex;gap:13px}
.ficons span{width:26px;height:26px;background:#fff;border-radius:4px}
.ficons span.round{border-radius:50%}
.frule{left:29px;top:62px;width:1107px;height:3px;background:#fff}
.copy{left:172px;top:80px;font-family:"Crimson Text",serif;font-size:23px;white-space:nowrap}
</style>
</head>
<body>

<header class="topbar">
  <div class="abs brand"><i></i>Plinthwave</div>
  <div class="abs phone">1-555-014-2290</div>
  <svg class="abs cart" width="28" height="26" viewBox="0 0 28 26" fill="none" stroke="#fff" stroke-width="2"><path d="M1 2h4l3 14h15l3-10H7"/><circle cx="10" cy="21" r="2"/><circle cx="21" cy="21" r="2"/></svg>
  <div class="abs badge">1</div>
  <div class="abs nav" style="left:655px">Products</div>
  <div class="abs nav" style="left:752px">About</div>
  <div class="abs nav" style="left:829px">Contact</div>
  <div class="abs avatar"></div>
  <div class="abs user">Rivenkit23</div>
</header>

<nav class="side">
  <a class="active" style="top:119px">Dashboard</a>
  <a style="top:177px">Vellumly</a>
  <a style="top:231px">Pictoraze</a>
  <a style="top:285px">Pictoraze</a>
  <a style="top:338px">Linkora</a>
  <a style="top:393px">Vidstream</a>
</nav>

<div class="abs stat" style="left:146px">98<br>Visit<svg width="100" height="72" viewBox="0 0 100 72" fill="none" stroke="#1a1a1a" stroke-width="3"><path d="M10 65v-14M40 65v-22M70 65v-34M97 65v-62M12 41C40 36 55 26 68 12M58 12h12v10"/></svg></div>
<div class="abs stat" style="left:380px">67<br>Imp<svg width="100" height="72" viewBox="0 0 100 72" fill="none" stroke="#1a1a1a" stroke-width="3"><path d="M10 65v-14M40 65v-22M70 65v-34M97 65v-62M12 41C40 36 55 26 68 12M58 12h12v10"/></svg></div>
<div class="abs stat" style="left:614px">90<br>Views<svg width="100" height="72" viewBox="0 0 100 72" fill="none" stroke="#1a1a1a" stroke-width="3"><path d="M10 65v-14M40 65v-22M70 65v-34M97 65v-62M12 41C40 36 55 26 68 12M58 12h12v10"/></svg></div>
<div class="abs stat" style="left:849px">98<br>Sales<svg width="100" height="72" viewBox="0 0 100 72" fill="none" stroke="#1a1a1a" stroke-width="3"><path d="M10 65v-14M40 65v-22M70 65v-34M97 65v-62M12 41C40 36 55 26 68 12M58 12h12v10"/></svg></div>

<h2 class="abs sec-title" style="top:258px">Ads Impact</h2>
<div class="abs underline" style="left:481px;top:297px;width:33px"></div>

<svg width="0" height="0" style="position:absolute">
  <defs>
    <linearGradient id="gPink" x1="0" y1="0" x2="0" y2="1"><stop offset="0" stop-color="#f0057f"/><stop offset="1" stop-color="#ec6fa8"/></linearGradient>
    <linearGradient id="gOrange" x1="1" y1="0" x2="0" y2="1"><stop offset="0" stop-color="#ff8a00"/><stop offset="1" stop-color="#ffc98a"/></linearGradient>
    <linearGradient id="gBlue" x1="0" y1="0" x2="0" y2="1"><stop offset="0" stop-color="#2a2a8c"/><stop offset="1" stop-color="#0a9be0"/></linearGradient>
    <linearGradient id="gRust" x1="1" y1="0" x2="0" y2="1"><stop offset="0" stop-color="#f07a10"/><stop offset="1" stop-color="#8a4a2a"/></linearGradient>
  </defs>
</svg>

<div class="abs donut" style="left:171px">
  <svg width="170" height="170" viewBox="0 0 170 170"><circle cx="85" cy="85" r="76" fill="none" stroke="var(--ring)" stroke-width="14"/><circle cx="85" cy="85" r="76" fill="none" stroke="url(#gPink)" stroke-width="14" stroke-dasharray="238.8 477.5" transform="rotate(-90 85 85) scale(1,-1) translate(0,-170)"/></svg>
  <div class="pct">50%</div>
  <div class="month">Febuary</div><div class="big">50%</div>
  <p class="blurb">Lorem ipsum dolor sit amet, consectetur adipisicing elit, sed do eiusmod tempor incididunt ut labore et dolore magna aliqua. Ut enim ad minim veniam, quis nostrud exercitation ullamco</p>
</div>
<div class="abs donut" style="left:380px">
  <svg width="170" height="170" viewBox="0 0 170 170"><circle cx="85" cy="85" r="76" fill="none" stroke="var(--ring)" stroke-width="14"/><circle cx="85" cy="85" r="76" fill="none" stroke="url(#gOrange)" stroke-width="14" stroke-dasharray="119.4 477.5" transform="rotate(90 85 85) scale(1,-1) translate(0,-170)"/></svg>
  <div class="pct">25%</div>
  <div class="month">March</div><div class="big">25%</div>
  <p class="blurb">Lorem ipsum dolor sit amet, consectetur adipisicing elit, sed do eiusmod tempor incididunt ut labore et dolore magna aliqua. Ut enim ad minim veniam, quis nostrud exercitation ullamco</p>
</div>
<div class="abs donut" style="left:587px">
  <svg width="170" height="170" viewBox="0 0 170 170"><circle cx="85" cy="85" r="76" fill="none" stroke="var(--ring)" stroke-width="14"/><circle cx="85" cy="85" r="76" fill="none" stroke="url(#gBlue)" stroke-width="14" stroke-dasharray="382 477.5" transform="rotate(-180 85 85)"/></svg>
  <div class="pct">80%</div>
  <div class="month">April</div><div class="big">80%</div>
  <p class="blurb">Lorem ipsum dolor sit amet, consectetur adipisicing elit, sed do eiusmod tempor incididunt ut labore et dolore magna aliqua. Ut enim ad minim veniam, quis nostrud exercitation ullamco</p>
</div>
<div class="abs donut" style="left:797px">
  <svg width="170" height="170" viewBox="0 0 170 170"><circle cx="85" cy="85" r="76" fill="none" stroke="var(--ring)" stroke-width="14"/><circle cx="85" cy="85" r="76" fill="none" stroke="url(#gRust)" stroke-width="14" stroke-dasharray="71.6 477.5" transform="rotate(-90 85 85) scale(1,-1) translate(0,-170)"/></svg>
  <div class="pct">15%</div>
  <div class="month">May</div><div class="big">15%</div>
  <p class="blurb">Lorem ipsum dolor sit amet, consectetur adipisicing elit, sed do eiusmod tempor incididunt ut labore et dolore magna aliqua. Ut enim ad minim veniam, quis nostrud exercitation ullamco</p>
</div>

<h2 class="abs sec-title" style="top:644px">Activity</h2>
<div class="abs underline" style="left:507px;top:684px;width:33px"></div>

<div class="abs chart-title">This week Activity</div>
<div class="abs legend" style="left:432px;top:731px">Current Year</div>
<div class="abs legend" style="left:432px;top:745px">Last Year</div>
<div class="abs" style="left:559px;top:731px;width:8px;height:8px;border-radius:50%;background:#14336e"></div>
<div class="abs" style="left:559px;top:745px;width:8px;height:8px;border-radius:50%;background:#0aa0e6"></div>

<svg class="abs activity-chart" style="left:160px;top:744px" width="448" height="336" viewBox="200 930 560 420" font-family="Montserrat, sans-serif" font-size="16">
  <g stroke="#e2e2e2" stroke-width="1">
    <path d="M297 955v333M347 955v333M397 955v333M447 955v333M497 955v333M547 955v333M597 955v333M647 955v333M697 955v333"/>
    <path d="M247 988h467M247 1021h467M247 1054h467M247 1087h467M247 1120h467M247 1153h467M247 1186h467M247 1219h467M247 1252h467"/>
  </g>
  <rect x="247" y="955" width="467" height="333" fill="none" stroke="#333" stroke-width="2"/>
  <g fill="#222" text-anchor="end">
    <text x="241" y="960">11</text><text x="241" y="993">10</text><text x="241" y="1026">9</text><text x="241" y="1059">8</text><text x="241" y="1092">7</text><text x="241" y="1125">6</text><text x="241" y="1158">5</text><text x="241" y="1191">4</text><text x="241" y="1224">3</text><text x="241" y="1257">2</text><text x="241" y="1290">1</text>
  </g>
  <g fill="#222" text-anchor="middle">
    <text x="267" y="1316">Jan</text><text x="320" y="1316">Feb</text><text x="372" y="1316">Apr</text><text x="426" y="1316">May</text><text x="476" y="1316">Jun</text><text x="525" y="1316">Jul</text><text x="582" y="1316">Aug</text><text x="632" y="1316">Sep</text><text x="683" y="1316">Oct</text><text x="737" y="1316">Nov</text>
  </g>
  <polyline fill="none" stroke="var(--line-light)" stroke-width="5" points="247,1205 268,1170 362,1147 432,1115 507,1152 527,1085 575,1043 647,958"/>
  <polyline fill="none" stroke="var(--line-dark)" stroke-width="5" points="262,1288 318,1258 347,1246 412,1243 490,1160 547,1186 565,1138 600,1103 665,1027 714,1023"/>
  <g fill="#666"><circle cx="274" cy="1177" r="6"/><circle cx="433" cy="1115" r="6"/><circle cx="507" cy="1152" r="6"/><circle cx="528" cy="1085" r="6"/><circle cx="647" cy="960" r="6"/></g>
  <g fill="var(--dot-orange)" stroke="#8a2a00" stroke-width="1"><circle cx="348" cy="1246" r="6"/><circle cx="493" cy="1165" r="6"/><circle cx="547" cy="1186" r="6"/><circle cx="566" cy="1138" r="6"/><circle cx="667" cy="1031" r="6"/></g>
  <path d="M498 1030h56q11 0 11 12q0 12-11 12h-22l-6 8-6-8h-22q-11 0-11-12q0-12 11-12z" fill="#4aa6c9" stroke="#bcd9a2" stroke-width="2"/>
  <text x="522" y="1048" fill="#dff" font-size="13" text-anchor="middle">$7.3</text>
</svg>

<div class="abs side-text" style="left:625px;top:754px">
  <h3 style="margin-left:0;width:370px">Current Year</h3>
  <p>Lorem ipsum dolor sit amet, consectetur adipisicing elit, sed do eiusmod tempor incididunt ut labore et dolore magna aliqua. Ut enim ad minim veniam, quis nostrud exercitation ullamco laboris nisi ut aliquip ex ea commodo consequat. Duis aute irure dolor in reprehenderit in voluptate velit esse cillum dolore eu fugiat nulla pariatur. Excepteur sint occaecat cupidatat non proident, sunt in culpa qui officia deserunt mollit anim id est laborum. Sed ut perspiciatis unde omnis iste natus error sit voluptatem accusantium doloremque laudantium, totam rem aperiam, eaque ipsa quae ab illo inventore veritatis et quasi architecto beatae vitae dicta sunt explicabo. Nemo enim ipsam voluptatem quia voluptas sit</p>
</div>
<div class="abs side-text" style="left:625px;top:912px">
  <h3 style="width:410px">Last Year</h3>
  <p>Lorem ipsum dolor sit amet, consectetur adipisicing elit, sed do eiusmod tempor incididunt ut labore et dolore magna aliqua. Ut enim ad minim veniam, quis nostrud exercitation ullamco laboris nisi ut aliquip ex ea commodo consequat. Duis aute irure dolor in reprehenderit in voluptate velit esse cillum dolore eu fugiat nulla pariatur. Excepteur sint occaecat cupidatat non proident, sunt in culpa qui officia deserunt mollit anim id est laborum. Sed ut perspiciatis unde omnis iste natus error sit voluptatem accusantium doloremque laudantium, totam rem aperiam, eaque ipsa quae ab illo inventore veritatis et quasi architecto</p>
</div>

<div class="abs chat">
  <svg width="38" height="30" viewBox="0 0 38 30" fill="none" stroke="#fff" stroke-width="3"><rect x="2" y="2" width="34" height="26" rx="4"/><path d="M3 4l16 13L35 4"/></svg>
  Chat Now!
</div>

<footer class="abs footer">
  <div class="abs flinks">About Contact Vellumly Laser Targeting Guide Questionnaires</div>
  <div class="abs ficons"><span></span><span class="round"></span><span></span></div>
  <div class="abs frule"></div>
  <div class="abs copy">Copyright © 2018 Morrowvane, LLC - All rights reserved. Privacy Policy | Terms of Service</div>
</footer>

</body>
</html>
```